Design for travel planning site (landing page and initial interaction)

We are creating a travel planning site and want to get a handful of the screens and interactions in place.

1- Landing page – vellumboard style
2- Getting started modals

We want to focus on material design and flat subtle details. In your design we need you to show some of these details.

The first page we will take inspiration from chirrup. We want to load the page with all of the masonry bricks in the background but we want them to be fuzzy with a modal overlay on top. In the modal we will welcome users to the platform. After a few seconds we will disappear the modal and show that it is now accessible in the menu. (it disappears in the direction of the menu item we expect the user to interact with next)
In each vellumboard type card we want the following meta details to be shown.

• Image,
• Name of place,
• rating (probably use numbers not stars),
• location (country or city),
• duration of trip (3 days, 6 weeks etc…)
• Person that “pinned” the trip (similar to how vellumboard really is)

We need calls to action for View, Save to favorites, add to existing trip (you can use iconography for these CTA’s)

As a part of your design we need both the initial state of the page, and then to see how you plan to do the fade and CTA to the menu area. (wayfarlo.com does something like this as seen in this video http://clipvessel.example/t/9QwLmRtz – the red dot and pulse)

Part 2 Getting started sequence

The next think we want to capture is the getting started modals. Users will use this to start the process of planning their trip. We want to take inspiration from http://www.journexa.example/ (load page and then click “Begin your journey here”) you will see the couple of steps they go through to get the users info and start the plan of the trip.

1- http://clipvessel.example/t/Hp83KdXv2n (there is a search typeahead that is pretty cool)
2- http://clipvessel.example/t/7TbNq2WsYe
3- In your last step for this I want to get what a form would look like in your modal with the other 2

I am a big fan of this material’ish design pattern http://www.pixelhaven.example/dashkit/forms/basic as seen on the forms on the right side. Where the placeholder text becomes the title of the input field.

Let me know any questions you have. We can use a fictitious company name in the comps called “Route Crafters”

```html
<!DOCTYPE html>
<html lang="en">
<head>
<meta charset="utf-8">
<title>Route Crafters — Welcome</title>
<link href="https://fonts.googleapis.com/css2?family=Open+Sans:wght@400;600;700&display=swap" rel="stylesheet">
<style>
  :root {
    --page-bg: #e9e9e9;
    --card-bg: #f4f4f4;
    --meta-line: #c9c9c9;
    --meta-line-soft: #dadada;
    --accent: #f0a35a;
    --modal-dark: #1c1c1c;
    --modal-mid: #3a3a3a;
    --text-light: #ffffff;
    --wash: rgba(255,255,255,0.18);
  }
  * { box-sizing: border-box; margin: 0; padding: 0; }
  html, body { width: 1200px; height: 675px; overflow: hidden; }
  body {
    position: relative;
    background: var(--page-bg);
    font-family: "Open Sans", sans-serif;
  }

  /* Blurred masonry wall */
  .wall {
    position: absolute;
    inset: -20px;
    filter: blur(5px);
  }
  .brick {
    position: absolute;
    width: 240px;
    background: var(--card-bg);
    overflow: hidden;
  }
  .brick-photo { width: 100%; height: 240px; }
  .row-two .brick-photo { height: 238px; }
  .brick-meta { padding: 8px 12px; height: 87px; position: relative; }
  .brick-tag {
    display: block; width: 34px; height: 6px;
    background: var(--accent); margin-bottom: 10px;
  }
  .brick-tag.right { position: absolute; right: 12px; top: 8px; }
  .brick-line {
    display: block; height: 7px; background: var(--meta-line);
    margin-bottom: 6px;
  }
  .brick-line.short { width: 60%; background: var(--meta-line-soft); }
  .brick-foot {
    position: absolute; left: 12px; right: 12px; bottom: 10px;
    display: flex; justify-content: space-between; align-items: center;
  }
  .brick-stats { display: block; width: 50px; height: 6px; background: var(--meta-line); }
  .brick-icon { display: block; width: 12px; height: 12px; background: #9a9a9a; border-radius: 2px; }

  .wall-wash { position: absolute; inset: 0; background: var(--wash); }

  /* Welcome modal */
  .welcome-modal {
    position: absolute;
    left: 284px; top: 104px;
    width: 603px; height: 373px;
    overflow: hidden;
    box-shadow: 0 6px 24px rgba(0,0,0,0.35);
  }
  .welcome-backdrop {
    position: absolute; inset: 0;
    background:
      radial-gradient(ellipse at 28% 92%, #4a4a4a 0%, rgba(40,40,40,0) 45%),
      radial-gradient(ellipse at 45% 20%, #2e2e2e 0%, rgba(20,20,20,0) 50%),
      linear-gradient(135deg, var(--modal-mid) 0%, var(--modal-dark) 55%, #0d0d0d 100%);
  }
  .welcome-copy {
    position: absolute; left: 131px; top: 116px;
    color: var(--text-light);
  }
  .welcome-kicker {
    font-size: 19px; font-weight: 400; letter-spacing: 0.5px;
    line-height: 1;
  }
  .welcome-brand {
    font-size: 42px; font-weight: 600; line-height: 1.1;
    letter-spacing: 0.2px; margin-top: 4px;
  }
  .welcome-tagline {
    font-size: 12.5px; font-weight: 700; letter-spacing: 0.4px;
    margin-top: 6px;
  }
</style>
</head>
<body>

<div class="wall" aria-hidden="true">
  <!-- row one -->
  <div class="brick" style="left:-167px; top:0;">
    <div class="brick-photo" role="img" aria-label="Travel photo" style="background:linear-gradient(160deg,#c9b9a8,#8a6e55);"></div>
    <div class="brick-meta"><span class="brick-tag"></span><span class="brick-line"></span><span class="brick-line short"></span></div>
  </div>
  <div class="brick" style="left:97px; top:0;">
    <div class="brick-photo" role="img" aria-label="Bright interior photo" style="background:linear-gradient(170deg,#eae7df,#d9d4c8 60%,#cfcac0);"></div>
    <div class="brick-meta"><span class="brick-tag"></span><span class="brick-line"></span><span class="brick-line short"></span><div class="brick-foot"><span class="brick-stats"></span><span class="brick-icon"></span></div></div>
  </div>
  <div class="brick" style="left:360px; top:0;">
    <div class="brick-photo" role="img" aria-label="Shelf with plants photo" style="background:linear-gradient(180deg,#e4e7e6,#9fb6b8 70%,#6f9aa3);"></div>
    <div class="brick-meta"><span class="brick-tag"></span><span class="brick-line"></span><span class="brick-line short"></span></div>
  </div>
  <div class="brick" style="left:627px; top:0;">
    <div class="brick-photo" role="img" aria-label="Wall print photo" style="background:linear-gradient(180deg,#f1eeee,#e9c9c9 50%,#efe9e9);"></div>
    <div class="brick-meta"><span class="brick-tag right"></span><span class="brick-line"></span><span class="brick-line short"></span></div>
  </div>
  <div class="brick" style="left:889px; top:0;">
    <div class="brick-photo" role="img" aria-label="Yellow side table photo" style="background:linear-gradient(180deg,#8c8478,#d7a94a 35%,#7fb1ac 70%,#6e6458);"></div>
    <div class="brick-meta"><span class="brick-tag right"></span><span class="brick-line"></span><span class="brick-line short"></span><div class="brick-foot"><span class="brick-stats"></span><span class="brick-icon"></span></div></div>
  </div>
  <div class="brick" style="left:1153px; top:0;">
    <div class="brick-photo" role="img" aria-label="Room photo" style="background:linear-gradient(180deg,#cfcac4,#6b4f45);"></div>
    <div class="brick-meta"><span class="brick-tag"></span><span class="brick-line"></span></div>
  </div>

  <!-- row two -->
  <div class="brick row-two" style="left:-167px; top:369px;">
    <div class="brick-photo" role="img" aria-label="Plant photo" style="background:linear-gradient(170deg,#7f9a58,#c4c9b2);"></div>
    <div class="brick-meta"><span class="brick-tag"></span><span class="brick-line"></span></div>
  </div>
  <div class="brick row-two" style="left:97px; top:369px;">
    <div class="brick-photo" role="img" aria-label="Wooden rack on blue wall photo" style="background:linear-gradient(180deg,#2f4a7a,#8a4a3a 45%,#b0542e 75%,#e0d6c8);"></div>
    <div class="brick-meta"><span class="brick-tag"></span><span class="brick-line"></span><span class="brick-line short"></span></div>
  </div>
  <div class="brick row-two" style="left:360px; top:369px;">
    <div class="brick-photo" role="img" aria-label="Wooden furniture photo" style="background:linear-gradient(180deg,#e8e2d8,#a8643a 55%,#7a3f22);"></div>
    <div class="brick-meta"><span class="brick-tag right"></span><span class="brick-line"></span><span class="brick-line short"></span></div>
  </div>
  <div class="brick row-two" style="left:627px; top:369px;">
    <div class="brick-photo" role="img" aria-label="Green plant in vase photo" style="background:linear-gradient(180deg,#f2f1ec,#a9b585 50%,#eceae3);"></div>
    <div class="brick-meta"><span class="brick-tag right"></span><span class="brick-line"></span><span class="brick-line short"></span></div>
  </div>
  <div class="brick row-two" style="left:889px; top:369px;">
    <div class="brick-photo" role="img" aria-label="Desk with blue cabinets photo" style="background:linear-gradient(180deg,#d8dcd8,#8fc07a 15%,#5f7f9c 45%,#cfd5db 80%);"></div>
    <div class="brick-meta"><span class="brick-tag right"></span><span class="brick-line"></span><span class="brick-line short"></span></div>
  </div>
  <div class="brick row-two" style="left:1153px; top:369px;">
    <div class="brick-photo" role="img" aria-label="Shelves photo" style="background:linear-gradient(180deg,#a8875f,#d8cfc2);"></div>
    <div class="brick-meta"><span class="brick-tag"></span><span class="brick-line"></span></div>
  </div>

  <div class="wall-wash"></div>
</div>

<section class="welcome-modal" aria-label="Welcome">
  <div class="welcome-backdrop" role="img" aria-label="Dark monochrome photo of a record turntable with people in the background"></div>
  <div class="welcome-copy">
    <p class="welcome-kicker">WELCOME TO</p>
    <h1 class="welcome-brand">Route Crafters</h1>
    <p class="welcome-tagline">A True Place To Provide First Class Service</p>
  </div>
</section>

</body>
</html>
```